Eco friendly Swedish beauty products sold in aluminum bottles - label design needed

We need help in designing a series of stick on labels for 80 ml (2.7 fl. oz.) aluminum bottles containing beauty products such as soaps, shampoo etc. The diameter of the bottle is 36 mm and the body of the bottles measures approx. 106 mm.
It is important for us that the label has a simplistic and clean feel with few colors (and the right ones!) and that the label helps amplify this product being both better and a more sustainable alternative to many of our plastic bottle competitors. The design and label should communicate the feel of an Eco-friendly, sustainable and modern brand of high quality - and with a Swedish concept.
We are using Montserrat font in our materials. Find attached information of preferred colors, the bottles and one example of our logotype. I am also available on e-mail should further information be needed.

Looking forward and very excited to receive your suggestions.
Note that we are expecting to start selling a series of approximately 10 different products where I will need one "master design" and then only smaller changes for each of the different products.

Target Market(s)

People whom are aware and not only look at price tag. Private and commercial market.

Industry/Entity Type

Beauty

Font styles to use
Other font styles liked:
• Montserrat

Requirements
Must have
• It must give the feel of being both better and a more sustainable alternative to many of our plastic bottle competitors.
Nice to have
• Simplistic. Clean. Clear.
Should not have
• Wrong colors, too complex designs.

```html
<!DOCTYPE html>
<html lang="en">
<head>
<meta charset="utf-8">
<title>Nordvik Care – Natural Shampoo Label Series</title>
<link rel="stylesheet" href="https://fonts.googleapis.com/css2?family=Montserrat:wght@400;500&display=swap">
<style>
  :root {
    --canvas: #efebe4;
    --brand-ink: #3a2f28;
    --moss: #6b7c3a;
    --stone: #dcdad6;
    --amber: #a05f14;
    --rust: #9c4a2e;
    --peach: #dfb597;
    --charcoal: #333333;
    --cream: #f4f0e8;
    --ink-dark: #1e1e1e;
    --ink-light: #ffffff;
    --ink-orange: #d9801e;
    --ink-amber: #a86a1c;
  }
  * { box-sizing: border-box; margin: 0; padding: 0; }
  html, body { width: 1200px; height: 803px; overflow: hidden; }
  body {
    position: relative;
    background: var(--canvas);
    font-family: "Montserrat", sans-serif;
  }

  /* Brand header */
  .brand-header {
    position: absolute;
    left: 690px;
    top: 100px;
    width: 480px;
    text-align: right;
    color: var(--brand-ink);
    font-weight: 400;
  }
  .brand-header__name {
    display: flex;
    align-items: center;
    justify-content: flex-end;
    gap: 18px;
    font-size: 42px;
    letter-spacing: 5px;
    line-height: 1;
  }
  .brand-header__dot {
    width: 16px; height: 16px;
    border-radius: 50%;
    background: var(--brand-ink);
  }
  .brand-header__country {
    margin-top: 22px;
    font-size: 16px;
    letter-spacing: 6px;
  }

  /* Label master design */
  .label {
    position: absolute;
    display: flex;
    flex-direction: column;
    align-items: center;
    width: 83px;
    height: 243px;
    padding-top: 1.3em;
    font-size: 10px;
    background: var(--bg);
    color: var(--ink);
    text-align: center;
  }
  .label--bottle { width: 114px; height: 334px; font-size: 13.7px; }

  .label__head {
    height: 12.2em;
    writing-mode: vertical-rl;
    transform: rotate(180deg);
    line-height: 1;
  }
  .label__brand {
    display: block;
    font-size: 1.55em;
    letter-spacing: 0.08em;
    font-weight: 400;
  }
  .label__country {
    display: block;
    margin-left: 0.8em;
    font-size: 0.45em;
    letter-spacing: 0.3em;
    text-align: end;
  }
  .label__mark {
    width: 1.5em; height: 1.5em;
    margin-top: 0.9em;
    border-radius: 50%;
    background: var(--mark);
  }
  .label__product {
    margin-top: 1.3em;
    font-size: 0.74em;
    white-space: nowrap;
  }
  .label__tagline {
    margin-top: 2.9em;
    font-size: 0.62em;
    line-height: 1.1;
  }
  .label__volume {
    margin-top: 1.6em;
    font-size: 0.52em;
  }

  /* Colourways */
  .c-moss-dark   { --bg: var(--moss);     --ink: var(--ink-dark);  --mark: var(--ink-dark); }
  .c-moss-light  { --bg: var(--moss);     --ink: var(--ink-light); --mark: var(--ink-light); }
  .c-stone-amber { --bg: var(--stone);    --ink: var(--ink-amber); --mark: var(--amber); }
  .c-stone-dark  { --bg: var(--stone);    --ink: var(--ink-dark);  --mark: var(--ink-dark); }
  .c-amber-dark  { --bg: var(--amber);    --ink: var(--ink-dark);  --mark: var(--ink-dark); }
  .c-amber-light { --bg: var(--amber);    --ink: var(--ink-light); --mark: var(--ink-light); }
  .c-char-orange { --bg: var(--charcoal); --ink: var(--ink-orange);--mark: var(--ink-orange); }
  .c-char-light  { --bg: var(--charcoal); --ink: var(--ink-light); --mark: var(--ink-light); }
  .c-rust-dark   { --bg: var(--rust);     --ink: var(--ink-dark);  --mark: var(--ink-dark); }
  .c-rust-light  { --bg: var(--rust);     --ink: var(--ink-light); --mark: var(--ink-light); }
  .c-peach-amber { --bg: var(--peach);    --ink: var(--ink-amber); --mark: var(--amber); }
  .c-peach-dark  { --bg: var(--peach);    --ink: var(--ink-dark);  --mark: var(--ink-dark); }
  .c-cream-amber { --bg: var(--cream);    --ink: var(--ink-amber); --mark: var(--amber); }
  .c-cream-dark  { --bg: var(--cream);    --ink: var(--ink-dark);  --mark: var(--ink-dark); }
</style>
</head>
<body>

<header class="brand-header">
  <div class="brand-header__name"><span class="brand-header__dot"></span>NORDVIK CARE</div>
  <div class="brand-header__country">SWEDEN</div>
</header>

<!-- Bottle-size labels -->
<section class="label label--bottle c-rust-light" style="left:55px; top:432px;">
  <div class="label__head"><span class="label__brand">NORDVIK CARE</span><span class="label__country">SWEDEN</span></div>
  <div class="label__mark"></div>
  <p class="label__product">NATURAL SHAMPOO</p>
  <p class="label__tagline">fresh &amp; beauty<br>from nature</p>
  <p class="label__volume">80 mL (2.7 FL OZ)</p>
</section>
<section class="label label--bottle c-amber-light" style="left:220px; top:410px;">
  <div class="label__head"><span class="label__brand">NORDVIK CARE</span><span class="label__country">SWEDEN</span></div>
  <div class="label__mark"></div>
  <p class="label__product">NATURAL SHAMPOO</p>
  <p class="label__tagline">fresh &amp; beauty<br>from nature</p>
  <p class="label__volume">80 mL (2.7 FL OZ)</p>
</section>
<section class="label label--bottle c-peach-dark" style="left:395px; top:416px;">
  <div class="label__head"><span class="label__brand">NORDVIK CARE</span><span class="label__country">SWEDEN</span></div>
  <div class="label__mark"></div>
  <p class="label__product">NATURAL SHAMPOO</p>
  <p class="label__tagline">fresh &amp; beauty<br>from nature</p>
  <p class="label__volume">80 mL (2.7 FL OZ)</p>
</section>

<!-- Colourway series, top row -->
<section class="label c-moss-dark" style="left:713px; top:272px;">
  <div class="label__head"><span class="label__brand">NORDVIK CARE</span><span class="label__country">SWEDEN</span></div>
  <div class="label__mark"></div>
  <p class="label__product">NATURAL SHAMPOO</p>
  <p class="label__tagline">fresh &amp; beauty<br>from nature</p>
  <p class="label__volume">80 mL (2.7 FL OZ)</p>
</section>
<section class="label c-moss-light" style="left:816px; top:271px;">
  <div class="label__head"><span class="label__brand">NORDVIK CARE</span><span class="label__country">SWEDEN</span></div>
  <div class="label__mark"></div>
  <p class="label__product">NATURAL SHAMPOO</p>
  <p class="label__tagline">fresh &amp; beauty<br>from nature</p>
  <p class="label__volume">80 mL (2.7 FL OZ)</p>
</section>
<section class="label c-stone-amber" style="left:914px; top:271px;">
  <div class="label__head"><span class="label__brand">NORDVIK CARE</span><span class="label__country">SWEDEN</span></div>
  <div class="label__mark"></div>
  <p class="label__product">NATURAL SHAMPOO</p>
  <p class="label__tagline">fresh &amp; beauty<br>from nature</p>
  <p class="label__volume">80 mL (2.7 FL OZ)</p>
</section>
<section class="label c-stone-dark" style="left:1013px; top:271px;">
  <div class="label__head"><span class="label__brand">NORDVIK CARE</span><span class="label__country">SWEDEN</span></div>
  <div class="label__mark"></div>
  <p class="label__product">NATURAL SHAMPOO</p>
  <p class="label__tagline">fresh &amp; beauty<br>from nature</p>
  <p class="label__volume">80 mL (2.7 FL OZ)</p>
</section>
<section class="label c-amber-dark" style="left:1107px; top:271px;">
  <div class="label__head"><span class="label__brand">NORDVIK CARE</span><span class="label__country">SWEDEN</span></div>
  <div class="label__mark"></div>
  <p class="label__product">NATURAL SHAMPOO</p>
  <p class="label__tagline">fresh &amp; beauty<br>from nature</p>
  <p class="label__volume">80 mL (2.7 FL OZ)</p>
</section>

<!-- Colourway series, bottom row -->
<section class="label c-char-orange" style="left:634px; top:539px;">
  <div class="label__head"><span class="label__brand">NORDVIK CARE</span><span class="label__country">SWEDEN</span></div>
  <div class="label__mark"></div>
  <p class="label__product">NATURAL SHAMPOO</p>
  <p class="label__tagline">fresh &amp; beauty<br>from nature</p>
  <p class="label__volume">80 mL (2.7 FL OZ)</p>
</section>
<section class="label c-char-light" style="left:728px; top:539px;">
  <div class="label__head"><span class="label__brand">NORDVIK CARE</span><span class="label__country">SWEDEN</span></div>
  <div class="label__mark"></div>
  <p class="label__product">NATURAL SHAMPOO</p>
  <p class="label__tagline">fresh &amp; beauty<br>from nature</p>
  <p class="label__volume">80 mL (2.7 FL OZ)</p>
</section>
<section class="label c-rust-dark" style="left:819px; top:539px;">
  <div class="label__head"><span class="label__brand">NORDVIK CARE</span><span class="label__country">SWEDEN</span></div>
  <div class="label__mark"></div>
  <p class="label__product">NATURAL SHAMPOO</p>
  <p class="label__tagline">fresh &amp; beauty<br>from nature</p>
  <p class="label__volume">80 mL (2.7 FL OZ)</p>
</section>
<section class="label c-peach-amber" style="left:913px; top:538px;">
  <div class="label__head"><span class="label__brand">NORDVIK CARE</span><span class="label__country">SWEDEN</span></div>
  <div class="label__mark"></div>
  <p class="label__product">NATURAL SHAMPOO</p>
  <p class="label__tagline">fresh &amp; beauty<br>from nature</p>
  <p class="label__volume">80 mL (2.7 FL OZ)</p>
</section>
<section class="label c-cream-amber" style="left:1011px; top:539px;">
  <div class="label__head"><span class="label__brand">NORDVIK CARE</span><span class="label__country">SWEDEN</span></div>
  <div class="label__mark"></div>
  <p class="label__product">NATURAL SHAMPOO</p>
  <p class="label__tagline">fresh &amp; beauty<br>from nature</p>
  <p class="label__volume">80 mL (2.7 FL OZ)</p>
</section>
<section class="label c-cream-dark" style="left:1110px; top:539px;">
  <div class="label__head"><span class="label__brand">NORDVIK CARE</span><span class="label__country">SWEDEN</span></div>
  <div class="label__mark"></div>
  <p class="label__product">NATURAL SHAMPOO</p>
  <p class="label__tagline">fresh &amp; beauty<br>from nature</p>
  <p class="label__volume">80 mL (2.7 FL OZ)</p>
</section>

</body>
</html>
```